Virtual Racing Community for Runners Needs a Refreshed Web Design

We are a STARTUP. The current website consists of 3 main pages that function well; however, they are not producing the proper conversions because we need a more professional look and better execution of our great ideas.

First page: landing page that needs to be intriguing, sleek, create urgency, incorporate our call to action and most importantly get the consumer to click a button to get to second page. www.strydelo.com

Second page: sign up page that incorporates our already existing postwren form that doesn't take the viewer away from the page on incorrect form field entry. On successful completion needs to inform the viewer to check the email and confirm (possibly in spam) and open third page. http://www.strydelo.com/beta.html

Third page: preorder page that allows the user prepurchase through a well working form through "www.getquoral.com." This interface works really well; however, the graphics and page need to really entice the viewer to buy. http://www.strydelo.com/preorder.html

And that's it!!! Simple 3 pages that function currently 95% how we want it, but really needs that creative touch to push it to the next level!

Contact us with any other questions!
Updates

Reason: I have provided numerous feedback and am awaiting redesigns. Have it narrowed down to 2 designers. Need time to vet with stakeholders.

Industry/Entity Type

Racing

```html
<!DOCTYPE html>
<html lang="en">
<head>
<meta charset="utf-8">
<title>Strydelo — Race With Fewer Roadblocks</title>
<link href="https://fonts.googleapis.com/css2?family=Oswald:wght@400;500;600&family=Arimo:wght@400;700&display=swap" rel="stylesheet">
<style>
  :root {
    --ink: #0c0c0c;
    --plum: #7a0e3e;
    --magenta: #9c1251;
    --red: #b5201a;
    --orange: #dc7b1a;
    --footer: #141414;
    --white: #ffffff;
    --grey-text: #4a4a4a;
    --icon: #2f2f2f;
  }
  * { box-sizing: border-box; margin: 0; padding: 0; }
  html, body { width: 1200px; height: 1053px; overflow: hidden; background: var(--white); }
  body { position: relative; font-family: "Arimo", Arial, sans-serif; color: var(--ink); }

  .hero {
    position: absolute; left: 0; top: 0; width: 1200px; height: 522px;
    background:
      radial-gradient(ellipse 320px 380px at 170px 250px, #d0206f 0%, #b01a5c 35%, rgba(60,30,40,0.0) 75%),
      radial-gradient(ellipse 500px 160px at 980px 470px, #f6c268 0%, rgba(246,194,104,0) 80%),
      linear-gradient(180deg, #e9e9e6 0%, #f4f3ef 45%, #c9b9a4 80%, #5b4a3e 100%);
  }
  .hero-content { position: absolute; left: 605px; top: 0; width: 560px; }
  .brand {
    position: absolute; top: 18px; left: 2px;
    font-family: "Oswald", sans-serif; font-weight: 600; font-size: 96px; line-height: 1;
    letter-spacing: 6px; color: var(--ink);
  }
  .headline {
    position: absolute; top: 142px; left: 0; white-space: nowrap;
    font-family: "Oswald", sans-serif; font-weight: 500; font-size: 46px; line-height: 1;
    color: var(--plum); letter-spacing: 0.5px;
  }
  .tagline {
    position: absolute; top: 193px; left: 0; white-space: nowrap;
    font-family: "Oswald", sans-serif; font-weight: 400; font-size: 39px; line-height: 1;
    color: var(--magenta); letter-spacing: 1px;
  }
  .event-title {
    position: absolute; top: 277px; left: 0; white-space: nowrap;
    font-family: "Oswald", sans-serif; font-weight: 500; font-size: 38px; line-height: 1;
    color: var(--ink);
  }
  .event-text { position: absolute; top: 325px; left: 3px; width: 370px; font-size: 14px; line-height: 17px; }
  .cta { position: absolute; top: 375px; left: 0; display: flex; height: 54px; text-decoration: none; }
  .cta-arrow { width: 60px; background: var(--ink); display: flex; align-items: center; justify-content: center; }
  .cta-label {
    width: 193px; background: var(--red); color: var(--white);
    font-family: "Oswald", sans-serif; font-weight: 600; font-size: 30px;
    display: flex; align-items: center; justify-content: center;
  }

  .card {
    position: absolute; left: 110px; top: 486px; width: 980px; height: 324px; background: var(--white);
    box-shadow: 0 14px 22px -8px rgba(0,0,0,0.12), 8px 0 14px -10px rgba(0,0,0,0.12), -8px 0 14px -10px rgba(0,0,0,0.12);
  }
  .news { display: flex; height: 104px; }
  .news-date {
    width: 98px; background: var(--orange); color: var(--white);
    display: flex; flex-direction: column; align-items: center; justify-content: center;
  }
  .date-day {
    width: 44px; height: 44px; border: 2px solid var(--white); border-radius: 50%;
    display: flex; align-items: center; justify-content: center;
    font-family: "Oswald", sans-serif; font-size: 22px;
  }
  .date-month { font-size: 14px; margin-top: 6px; }
  .news-body { flex: 1; background: var(--red); color: var(--white); padding: 14px 16px 0 16px; }
  .news-title { font-size: 17px; margin-bottom: 10px; }
  .news-text { font-size: 13px; line-height: 16px; }

  .features { position: absolute; top: 174px; left: 0; width: 980px; }
  .feature { position: absolute; top: 0; width: 240px; }
  .feature-icon { position: absolute; left: 0; top: 0; }
  .feature-title { position: absolute; left: 59px; top: -2px; font-size: 18px; color: #333; white-space: nowrap; }
  .feature-text { position: absolute; left: 60px; top: 25px; width: 240px; font-size: 13px; line-height: 16px; color: var(--grey-text); }
  .view-btn { position: absolute; left: 60px; top: 84px; display: flex; height: 25px; text-decoration: none; }
  .view-label { width: 49px; background: var(--red); color: var(--white); font-size: 12px; display: flex; align-items: center; padding-left: 11px; }
  .view-arrow { width: 28px; background: var(--ink); display: flex; align-items: center; justify-content: center; }

  .site-footer { position: absolute; left: 0; top: 862px; width: 1200px; height: 128px; background: var(--footer); color: var(--white); }
  .connect-title { position: absolute; left: 113px; top: 28px; font-family: "Oswald", sans-serif; font-size: 25px; letter-spacing: 0.5px; }
  .social { position: absolute; left: 115px; top: 71px; display: flex; gap: 20px; list-style: none; }
  .social li { width: 40px; height: 40px; border: 2px solid var(--white); border-radius: 50%; }
  .contact { position: absolute; left: 829px; top: 32px; }
  .contact-row { display: flex; align-items: center; gap: 12px; }
  .contact-icon { width: 32px; height: 32px; border: 2px solid var(--white); border-radius: 50%; display: flex; align-items: center; justify-content: center; }
  .address { font-size: 12px; line-height: 18px; color: #dcdcdc; }
  .phone { font-size: 23px; color: #d0d0d0; margin-top: 12px; }
  .legal-bar { position: absolute; left: 0; top: 990px; width: 1200px; height: 48px; background: var(--orange); color: var(--white); font-size: 11px; }
  .copyright { position: absolute; left: 115px; top: 18px; }
  .legal-links { position: absolute; right: 115px; top: 18px; }
  .base-strip { position: absolute; left: 0; top: 1038px; width: 1200px; height: 15px; background: var(--footer); }
</style>
</head>
<body>
  <header class="hero" role="img" aria-label="Photo of a runner in a pink jacket sprinting past a blurred city at sunset">
  </header>

  <section class="hero-content">
    <div class="brand">STRYDELO</div>
    <h1 class="headline">RACE WITH FEWER ROADBLOCKS</h1>
    <p class="tagline">MONITOR. MEASURE. MASTER.</p>
    <h2 class="event-title">CHICAGO BETA RUN WEEK 2</h2>
    <p class="event-text">For a limited time be the first to receive early access and receive a Real Life Beta Tester t-shirt.</p>
    <a class="cta" href="#register">
      <span class="cta-arrow">
        <svg width="24" height="18" viewBox="0 0 24 18"><path d="M1 9h20M13 2l8 7-8 7" stroke="#fff" stroke-width="3" fill="none"/></svg>
      </span>
      <span class="cta-label">REGISTER NOW</span>
    </a>
  </section>

  <main class="card">
    <article class="news">
      <div class="news-date">
        <span class="date-day">23</span>
        <span class="date-month">AUG</span>
      </div>
      <div class="news-body">
        <h3 class="news-title">Latest Virtual Run</h3>
        <p class="news-text">Lorem ipsum dolor sit amet, consectetur adipisicing elit, sed do eiusmod tempor incididunt ut labore et dolore magna aliqua. Ut enim ad minim veniam, quis nostrud exercitation ullamco laboris nisi ut aliquip ex ea commodo consequat.</p>
      </div>
    </article>

    <section class="features">
      <div class="feature" style="left:25px">
        <svg class="feature-icon" width="42" height="44" viewBox="0 0 42 44" fill="var(--icon)">
          <path d="M10 2h22v12a11 11 0 0 1-22 0z"/>
          <path d="M10 6H3v5a8 8 0 0 0 8 7M32 6h7v5a8 8 0 0 1-8 7" stroke="var(--icon)" stroke-width="3" fill="none"/>
          <rect x="18" y="24" width="6" height="8"/><rect x="11" y="32" width="20" height="4"/><rect x="9" y="37" width="24" height="5"/>
        </svg>
        <h4 class="feature-title">freebies and giveaways</h4>
        <p class="feature-text">Duis aute irure dolor in reprehenderit in voluptate velit esse cillum dolore eu fugiat nulla pariatur.</p>
        <a class="view-btn" href="#"><span class="view-label">view</span><span class="view-arrow"><svg width="12" height="10" viewBox="0 0 12 10"><path d="M0 5h10M6 1l4 4-4 4" stroke="#fff" stroke-width="1.8" fill="none"/></svg></span></a>
      </div>
      <div class="feature" style="left:345px">
        <svg class="feature-icon" width="50" height="54" viewBox="0 0 50 54" fill="var(--icon)">
          <rect x="2" y="28" width="46" height="5"/><rect x="22" y="33" width="3" height="20"/>
          <path d="M6 20l14-8 10 4 10-6 4 4-14 9-10-4-12 7z"/>
        </svg>
        <h4 class="feature-title">run at your own pace</h4>
        <p class="feature-text">You can walk, jog, skip or run the distance of your choice. You can complete your race at the gym ...</p>
        <a class="view-btn" href="#"><span class="view-label">view</span><span class="view-arrow"><svg width="12" height="10" viewBox="0 0 12 10"><path d="M0 5h10M6 1l4 4-4 4" stroke="#fff" stroke-width="1.8" fill="none"/></svg></span></a>
      </div>
      <div class="feature" style="left:668px">
        <svg class="feature-icon" width="52" height="50" viewBox="0 0 52 50" fill="none" stroke="var(--icon)" stroke-width="3.5">
          <circle cx="17" cy="12" r="9"/><circle cx="38" cy="22" r="11"/><circle cx="16" cy="33" r="13"/>
          <text x="16" y="39" font-family="Arimo, sans-serif" font-size="16" font-weight="700" fill="var(--icon)" stroke="none" text-anchor="middle">$</text>
          <text x="38" y="27" font-family="Arimo, sans-serif" font-size="13" font-weight="700" fill="var(--icon)" stroke="none" text-anchor="middle">$</text>
        </svg>
        <h4 class="feature-title">discounts</h4>
        <p class="feature-text" style="width:210px">If you have 10 or more runners interested in participating in one of our races, please contact us and ...</p>
        <a class="view-btn" href="#"><span class="view-label">view</span><span class="view-arrow"><svg width="12" height="10" viewBox="0 0 12 10"><path d="M0 5h10M6 1l4 4-4 4" stroke="#fff" stroke-width="1.8" fill="none"/></svg></span></a>
      </div>
    </section>
  </main>

  <footer class="site-footer">
    <h3 class="connect-title">CONNECT WITH US</h3>
    <ul class="social" aria-label="Social channels">
      <li aria-label="Social link"></li><li aria-label="Social link"></li><li aria-label="Social link"></li><li aria-label="Social link"></li>
    </ul>
    <div class="contact">
      <div class="contact-row">
        <span class="contact-icon"><svg width="18" height="16" viewBox="0 0 18 16" fill="#fff"><path d="M9 0l9 8h-3v8h-4v-5H7v5H3V8H0z"/></svg></span>
        <p class="address">4820 Lakeview Terrace Suite 310<br>Brookfield, Oregon 970215</p>
      </div>
      <div class="contact-row">
        <span class="contact-icon" style="margin-top:12px"><svg width="16" height="16" viewBox="0 0 16 16" fill="#fff"><path d="M3 0l3 4-2 2c1 2 4 5 6 6l2-2 4 3-2 3C8 16 0 8 0 3z"/></svg></span>
        <p class="phone">012-555-0147</p>
      </div>
    </div>
  </footer>
  <div class="legal-bar">
    <p class="copyright">© Copyright 2014 Strydelo. All Rights Reserved</p>
    <p class="legal-links">Policy | Terms</p>
  </div>
  <div class="base-strip"></div>
</body>
</html>
```